Website Redesign for Technology Focused Investment Bank

We need a website redesign for a technology and digital media focused investment banking firm. Think modern and forward thinking yet stable and smart. We provide mergers and acquisitions advisory services to our clients. Our target market are CEO's and CFO's (senior executives) that run and operate technology firms.

Kestrel Bay Advisors - www.kestrelbayadvisors.example

We are headquartered in Los Angeles, CA. Please do NOT use the Brindle Arch for anything.

We have the content and can update the photos as well.

We are looking for a "template" website we can update and edit with ease.

A competitive firm's website is: www.dunmoregrey.example Not sure I like it but I want it to look way better then this one.

Looking for a more modern version. Not too stuffy and conservative, please. Elegant, smart, updated and progressive/modern.
Updates

Color preferences:  Blue's including matching logo color. Grey's. You can add other colors if it flows well and looks clean and nice.

Menu:  Drop Down

Open to platform...please use one that most people can use, is reasonably priced if I need to buy it, and easy to update monthly and sometimes weekly.

Please use this website as a good example of what we are looking for (or similar version of it): www.plorvex.example

Thanks!
Tobias R.

We are reviewing all submissions and will select one this week. Thank you everyone for your outstanding and creative designs you have sent us. We really appreciate it.

Thanks for everyone's hard work and creative input into our website design. We really appreciate it!

Target Market(s)

CEO's and CFO's, Entrepreneurs and Board Members of Technology Companies.

Industry/Entity Type

Investment

Font styles to use
Sans Serif

Colors
33a6d7
0492cd
0555a3
3176b5
85abd2
333333
5c5c5c
757575

Requirements
Must have
• Links to social media including Chirper, LinkedIn, Google+, Gatherly, etc.

Must try to match logo color
Should not have
• No conservative, old looking colors or background. For example, no green marble look.

```html
<!DOCTYPE html>
<html lang="en">
<head>
<meta charset="utf-8">
<title>Kestrel Bay Advisors</title>
<link rel="stylesheet" href="https://fonts.googleapis.com/css2?family=Open+Sans:wght@400;600;700&family=Playfair+Display:ital,wght@1,700&display=swap">
<style>
:root{
  --blue-bright:#0492cd;
  --blue-sky:#33a6d7;
  --blue-deep:#0555a3;
  --blue-mid:#3176b5;
  --blue-soft:#85abd2;
  --ink:#333333;
  --ink-mid:#5c5c5c;
  --ink-soft:#757575;
  --rule:#dcdcdc;
  --panel:#f3f3f3;
  --footer:#2e2e2e;
}
*{margin:0;padding:0;box-sizing:border-box}
html,body{width:768px;height:1200px;overflow:hidden;background:#fff}
body{position:relative;font-family:'Open Sans',sans-serif;color:var(--ink)}
.abs{position:absolute}

/* header */
.header{left:0;top:0;width:768px;height:66px;background:#fff}
.brand{left:64px;top:10px;display:flex;align-items:center;gap:12px}
.brand-dot{width:52px;height:52px;border-radius:50%;background:var(--blue-mid)}
.brand-name{font-size:14px;color:var(--blue-deep);font-weight:400}
.tagline{left:330px;top:23px;width:178px;text-align:center;font-size:12px;font-weight:600;color:var(--blue-deep);line-height:15px}
.search{left:541px;top:22px;width:155px;height:29px;border:1px solid #cfcfcf;border-radius:2px;background:#f7f7f7;font-size:8px;color:#888;padding:9px 10px}
.search svg{position:absolute;right:9px;top:8px}

/* nav */
.nav{left:0;top:66px;width:768px;height:34px;background:linear-gradient(#2f86d2,#1462b4);border-bottom:2px solid #0d4f98;display:flex;padding-left:64px}
.nav a{display:block;height:32px;line-height:32px;text-align:center;color:#fff;font-size:11px;text-decoration:none;border-right:1px solid rgba(0,0,0,.18);box-shadow:1px 0 0 rgba(255,255,255,.15)}
.nav a:first-child{border-left:1px solid rgba(0,0,0,.18)}

/* hero */
.hero{left:0;top:102px;width:768px;height:283px;background:linear-gradient(100deg,#f4f4f4 0%,#d9dadb 38%,#8fa3b8 55%,#c9d3dd 70%,#7c8ea3 85%,#a9b6c4 100%)}
.dropdown{left:258px;top:103px;width:140px;background:rgba(8,92,180,.92);padding-top:10px}
.dropdown div{height:26px;line-height:26px;font-size:9.5px;color:#fff;padding-left:14px;border-bottom:1px solid rgba(255,255,255,.15)}
.dropdown div:last-child{border-bottom:none}
.caption{left:0;top:257px;width:301px;height:93px;background:rgba(40,40,40,.88);border:1px solid #777;border-left:none;color:#fff;font-size:14px;line-height:23px;text-align:right;padding:6px 14px}
.arrow{top:360px;width:20px;height:20px;background:#555}
.arrow svg{display:block;margin:6px auto}

/* band */
.band{left:0;top:385px;width:768px;height:64px;background:var(--blue-bright)}
.band-text{left:72px;top:407px;font-size:13.5px;font-weight:600;color:#fff}
.social{top:409px;width:20px;height:20px;border-radius:50%;background:#222;border:1px solid #555}

/* tiles */
.tiles{left:0;top:449px;width:768px;height:144px;background:var(--panel)}
.tile{top:467px;width:180px;height:107px}
.tile .label{position:absolute;left:0;bottom:0;width:100%;height:23px;background:rgba(40,40,40,.72);color:#fff;font-size:11.5px;font-weight:600;line-height:23px;padding-left:12px}

/* content */
.h2{font-size:12px;font-weight:600;color:var(--blue-bright)}
.rule{height:1px;background:var(--rule)}
.photo{left:71px;top:637px;width:149px;height:210px;background:radial-gradient(ellipse at 55% 45%,#3a3d44,#060606 70%)}
.copy{left:232px;top:635px;width:218px;font-size:8.3px;line-height:11.6px;color:var(--ink)}
.copy p{margin-bottom:11.6px}
.btn{width:61px;height:20px;background:var(--blue-bright);border:1px solid #0a78b0;box-shadow:0 0 0 2px #d9eef8;color:#fff;font-size:7.5px;font-weight:700;text-align:center;line-height:18px}
.svc-intro{left:486px;top:635px;width:205px;font-size:8.3px;line-height:10.5px}
.svc-list{left:489px;top:676px;list-style:none}
.svc-list li{height:20.5px;font-size:8.3px;display:flex;align-items:center;gap:12px}
.svc-list i{width:7px;height:7px;background:var(--blue-mid);position:relative}
.svc-list i::after{content:"";position:absolute;left:2px;top:1.5px;border-left:3px solid #fff;border-top:2px solid transparent;border-bottom:2px solid transparent}

/* updates */
.updates{left:65px;top:869px;width:631px;height:85px;border:1px solid #ddd;background:linear-gradient(#fdfdfd,#efefef)}
.updates-title{left:70px;top:896px;font-family:'Playfair Display',serif;font-style:italic;font-weight:700;font-size:20px;color:var(--blue-deep)}
.field{top:898px;width:156px;height:27px;border:1px solid #ccc;background:#fff;font-size:7px;font-style:italic;color:#555;padding:9px 6px}
.subscribe{left:606px;top:898px;width:80px;height:27px;background:var(--blue-deep);color:#fff;font-family:'Playfair Display',serif;font-style:italic;font-size:10px;text-align:center;line-height:27px;letter-spacing:.3px}

/* footer */
.footer{left:0;top:971px;width:768px;height:229px;background:var(--footer)}
.footer-bottom{left:0;top:1143px;width:768px;height:57px;background:#3a3a3a}
.f-head{font-size:11.5px;color:#ddd;letter-spacing:.3px}
.f-rule{height:1px;background:#555}
.f-text{font-size:8px;color:#d8d8d8;line-height:11.5px}
.f-link{color:var(--blue-sky)}
.avatar{width:31px;height:31px;background:linear-gradient(135deg,#d99a5c,#8a5a3a)}
.follow{left:72px;top:1016px;display:flex;gap:4px;font-size:7px}
.follow span{background:#fff;color:#222;padding:1px 5px;border-radius:2px}
.c-icon{width:12px;height:12px}
.sq{width:13px;height:13px;border-radius:2px}
.copyright{right:84px;top:1164px;font-size:7.5px;color:#ddd;text-align:right;line-height:15px}
</style>
</head>
<body>

<header class="abs header">
  <div class="abs brand"><span class="brand-dot"></span><span class="brand-name">Kestrel Bay Advisors</span></div>
  <div class="abs tagline">Technology and Digital Media Investment Banking</div>
  <div class="abs search">Search
    <svg width="12" height="12" viewBox="0 0 12 12"><circle cx="4.5" cy="4.5" r="3.3" fill="none" stroke="#888" stroke-width="1.4"/><line x1="7" y1="7" x2="11" y2="11" stroke="#888" stroke-width="1.8"/></svg>
  </div>
</header>

<nav class="abs nav">
  <a style="width:89px">Home</a>
  <a style="width:104px">About Us</a>
  <a style="width:96px">Services</a>
  <a style="width:121px">Transactions</a>
  <a style="width:111px">News+Blog</a>
  <a style="width:112px">Contact Us</a>
</nav>

<div class="abs hero" role="img" aria-label="Upward view of a modern glass office tower against a pale sky"></div>
<svg class="abs" style="left:266px;top:98px" width="12" height="6"><polygon points="0,6 6,0 12,6" fill="#0b5cb4"/></svg>
<div class="abs dropdown">
  <div>Research</div><div>Private Equity</div><div>Recommendations</div><div>About the Founder</div><div>Careers</div>
</div>
<div class="abs caption">Investment Banking and M&amp;A Advisory<br>for Software, IT Services and<br>Digital Media Companies</div>
<div class="abs arrow" style="left:256px"><svg width="6" height="8"><polyline points="5,0 1,4 5,8" fill="none" stroke="#fff" stroke-width="1.6"/></svg></div>
<div class="abs arrow" style="left:279px;background:#888"><svg width="6" height="8"><polyline points="1,0 5,4 1,8" fill="none" stroke="#fff" stroke-width="1.6"/></svg></div>

<div class="abs band"></div>
<div class="abs band-text">Partner With Us. Succeed With Us. Learn More About Us.</div>
<div class="abs social" style="left:596px"></div>
<div class="abs social" style="left:620px"></div>
<div class="abs social" style="left:644px"></div>
<div class="abs social" style="left:668px"></div>

<section class="abs tiles"></section>
<div class="abs tile" style="left:78px;background:linear-gradient(120deg,#e8edf2,#6d7a88 40%,#1f6fb8 70%,#cfd7df)" role="img" aria-label="Server racks beside a monitor showing a world map"><div class="label">Software</div></div>
<div class="abs tile" style="left:290px;background:linear-gradient(90deg,#2c4b73,#b9d2e6 45%,#e9f0f6 55%,#4a6d95)" role="img" aria-label="Two hands passing a network cable between server rows"><div class="label">IT Services</div></div>
<div class="abs tile" style="left:502px;background:linear-gradient(135deg,#dbe7f4,#4a86c8 50%,#1d4f99)" role="img" aria-label="Blue abstract grid of digital characters"><div class="label">Internet and Digital Mediag</div></div>

<div class="abs h2" style="left:71px;top:606px">Why Us?</div>
<div class="abs rule" style="left:71px;top:626px;width:382px"></div>
<div class="abs photo" role="img" aria-label="Portrait of the founder in a dark suit, arms crossed"></div>
<div class="abs copy">
  <p>We are an independent investment bank and M&amp;A advisory firm focused exclusively on the global Technol­ogy and Digital Media sectors. Specifically, we execute mergers and acquisitions for the Software, IT Services, Internet and Digital Media industry sectors.</p>
  <p>Our professionals have completed over $20 billion in transactions to date and have experience in investment banking, private equity and capital markets from lead­ing firms. We are experts in complex M&amp;A transactions of most shapes and sizes and have deep industry expertise.</p>
  <p>We advise companies, entrepreneurs, majority share­holders and leading institutions on complex strategic and financial transactions including mergers, acquisi-</p>
</div>
<div class="abs btn" style="left:233px;top:826px">MORE &gt;&gt;</div>

<div class="abs h2" style="left:481px;top:606px">Services</div>
<div class="abs rule" style="left:481px;top:626px;width:198px"></div>
<div class="abs svc-intro">M&amp;A is the foundation and focus of our firm. Our services include evaluating potential targets or merger partners, providing valuation analyses</div>
<ul class="abs svc-list">
  <li><i></i>Buy-Side Mergers and Acquisitions</li>
  <li><i></i>Sell-Side Mergers and Acquisitions</li>
  <li><i></i>Recapitalizations and Restructuring's</li>
  <li><i></i>Equity and Debt Buyout Financing (Advisory)</li>
  <li><i></i>Spin-Offs and Asset Sales</li>
  <li><i></i>Strategic and Corporate Finance Advisory</li>
  <li><i></i>Fairness Opinions and Valuations</li>
</ul>
<div class="abs btn" style="left:484px;top:825px">MORE &gt;&gt;</div>

<div class="abs updates"></div>
<div class="abs updates-title">Our M&amp;A Updates :</div>
<div class="abs field" style="left:252px">Enter Your Name :</div>
<div class="abs field" style="left:429px">Pass word :</div>
<div class="abs subscribe">SUBSCRIBE</div>

<footer class="abs footer"></footer>
<div class="abs footer-bottom"></div>

<svg class="abs" style="left:73px;top:986px" width="22" height="18" viewBox="0 0 22 18"><circle cx="11" cy="9" r="8" fill="var(--blue-sky)"/></svg>
<div class="abs" style="left:103px;top:987px;font-size:13.5px;color:var(--blue-sky)">Latest Chirp</div>
<div class="abs follow"><span>Follow @KestrelTechDeals</span><span>1,316 followers</span></div>

<div class="abs avatar" style="left:73px;top:1040px" role="img" aria-label="Small profile photo"></div>
<div class="abs f-text" style="left:111px;top:1038px">&nbsp;Kestrel Bay<br><span class="f-link">@KestrelTechDeals</span><br>M&amp;A - Best Start to Year Since 2011<br><span class="f-link">http://lnk.example/k7Qb</span></div>
<div class="abs avatar" style="left:73px;top:1099px;background:linear-gradient(135deg,#e8c48a,#9a6a58)" role="img" aria-label="Small profile photo"></div>
<div class="abs f-text" style="left:111px;top:1097px">&nbsp;Kestrel Bay<br><span class="f-link">@KestrelTechDeals</span><br>M&amp;A - Best Start to Year Since 2011<br><span class="f-link">http://lnk.example/k7Qb</span></div>

<div class="abs f-head" style="left:320px;top:993px">CONTACT US</div>
<div class="abs f-rule" style="left:320px;top:1010px;width:148px"></div>
<svg class="abs" style="left:318px;top:1024px" width="12" height="15" viewBox="0 0 12 15"><path d="M6 14 C2 9 1 7 1 5.5 A5 5 0 0 1 11 5.5 C11 7 10 9 6 14Z" fill="none" stroke="#777" stroke-width="1.2"/><circle cx="6" cy="5.5" r="1.8" fill="#777"/></svg>
<div class="abs f-text" style="left:346px;top:1022px">Kestrel Bay Advisors, LLC<br>4120 Larkspur Ave, Suite 300<br>Los Angeles, CA 90012<br>United States of America</div>
<svg class="abs" style="left:320px;top:1075px" width="12" height="15" viewBox="0 0 12 15"><path d="M2 1 L5 1 L6 4 L4 5.5 C5 8 6 9.5 8 11 L9.5 9 L12 10.5 L11 14 C6 13 2 8 2 1Z" fill="none" stroke="#777" stroke-width="1.1"/></svg>
<div class="abs f-text" style="left:346px;top:1080px">+1 (310) 555-0147</div>
<svg class="abs" style="left:319px;top:1107px" width="13" height="10" viewBox="0 0 13 10"><rect x=".5" y=".5" width="12" height="9" fill="none" stroke="#777"/><polyline points=".5,.5 6.5,5.5 12.5,.5" fill="none" stroke="#777"/></svg>
<div class="abs f-text" style="left:346px;top:1106px">deals@kestrelbayadvisors.example</div>

<div class="abs f-head" style="left:578px;top:994px">CONNECT WITH US</div>
<div class="abs f-rule" style="left:578px;top:1013px;width:110px"></div>
<div class="abs sq" style="left:581px;top:1029px;background:var(--blue-mid)"></div>
<div class="abs f-text" style="left:607px;top:1029px">Gatherly</div>
<div class="abs sq" style="left:581px;top:1052px;background:var(--blue-sky)"></div>
<div class="abs f-text" style="left:607px;top:1052px">Chirper</div>
<div class="abs sq" style="left:581px;top:1075px;background:var(--blue-deep)"></div>
<div class="abs f-text" style="left:608px;top:1075px">Linkwork</div>
<div class="abs sq" style="left:581px;top:1098px;background:var(--ink-soft)"></div>
<div class="abs f-text" style="left:608px;top:1098px">Orbit +1</div>

<div class="abs copyright">© 2014 kestrelbayadvisors.example, All rights reserved<br>X2</div>

</body>
</html>
```